Stalwart Noble Alloys Foundries Business Cards

Business Card Design Description
We are wanting to have a new business card designed for our company as we go to a convention. We want to balance business/Modern with elegance and beauty. Our company sells highend jewelry pieces. We want to utilize the colors of Black and Gold and have gold foiled fonts to be physically printed on the business cards.
We also would like to have space to write notes on the back side of the business card. When we meet people at jewelry conventions we would like to write notes if possible.
Here are websites and designs that we like the look and feel of these companies and you can use these as design ideas.
https://www.bellwynne.com
https://www.morvandel.com/en-us/home
Here is our company website link
www.stalwartnaf.com
I also up loaded two versions of our logo.
- Update 4.26.22
I have uploaded photos of a business card we like. this card has raised embossed letters that you can feel. the raise letters are like a plastic but we don't need to use that...I uploaded to show you that we like the experience of the client feeling the characters of the logo. we also would like to have the material as a satin or some material very soft.
- Maybe we can get designs with beautiful gold foiling and raised characters and logos. we like simplicity...not busy but an elegant design. We need to write notes and would like a section where we can write notes. but we want an elegant style and the client has an experience with the feel of the card when they touch the card.
Colors
- Main colors Black & Gold
- white or light colors for small notes section.
Specialty ideals and things we would like to see based on your design styles.
- raised fonts
- raised logos
- gold foiling
- satin/soft finish on the card material.
we are wanting to design a business card that looks elegant and clean. When the client is handed the business card we want them to physically experience the business card as well by touching the raised logos or fonts and the base material is soft satin. I hope this helps with further designs.
thank you all
We uploaded a new contact layout that we have designed in our office. we would like to see how this would look on your designs.
thank you
I just finished uploading the Contact Layout. the colors are just examples. please use this layout as an idea and use colors based on the feed back we have given each of you personally.
Contact Information for Business Card
we need an area to write notes, we would like to have our logos or the diamond of our logo or the business card to have embossed sections to the business card so when the customer touches the card they can feel the logo. we would also like sections of our business card to have gold foiling. we would also like to use a satin soft paper with our card. when the client touches the card its super soft and high quality
Requirements
Must have
- we would like to have our logos or the diamond of our logo or the business card to have embossed sections to the business card so when the customer touches the card they can feel the logo. we would also like sections of our business card to have gold foiling. we would also like to use a satin soft paper with our card. when the client touches the card its super soft and high quality
Nice to have
- we would like to have our logos or the diamond of our logo or the business card to have embossed sections to the business card so when the customer touches the card they can feel the logo. we would also like sections of our business card to have gold foiling.

```html
<!DOCTYPE html>
<html lang="en">
<head>
<meta charset="utf-8">
<title>Stalwart Noble Alloys Foundries Business Cards</title>
<link rel="stylesheet" href="https://fonts.googleapis.com/css2?family=Cinzel:wght@600&family=Montserrat:wght@400;500&display=swap">
<style>
  :root {
    --stage: #d9d9d9;
    --card-black: #1f1f1f;
    --card-white: #f6f6f4;
    --gold: #c99a2e;
    --ink-light: #f2f2f2;
    --title-tint: #cfe3ee;
    --rule-dark: #3a3a3a;
    --dot-rule: #8a8a8a;
    --ink-dark: #222222;
  }
  * { box-sizing: border-box; margin: 0; padding: 0; }
  html, body { width: 1200px; height: 800px; overflow: hidden; }
  body {
    background: var(--stage);
    font-family: "Montserrat", sans-serif;
    position: relative;
  }
  .card {
    position: absolute;
    width: 525px;
    height: 300px;
    border-radius: 18px;
    top: 250px;
    box-shadow: 0 10px 24px rgba(0,0,0,0.22);
    overflow: hidden;
  }
  .card-front {
    left: 50px;
    background: var(--card-black);
    border-bottom: 7px solid var(--gold);
  }
  .brand {
    position: absolute;
    left: 0; right: 0;
    display: flex;
    justify-content: center;
    align-items: center;
    gap: 10px;
    font-family: "Montserrat", sans-serif;
    font-weight: 500;
    color: var(--gold);
  }
  .brand-mark {
    width: 10px; height: 10px;
    border-radius: 50%;
    background: var(--gold);
    flex: none;
  }
  .brand-name { font-size: 20px; letter-spacing: 1px; line-height: 1; text-transform: uppercase; }
  .card-front .brand { top: 72px; }
  .person { position: absolute; left: 40px; top: 172px; width: 210px; text-align: center; }
  .person-name {
    font-family: "Cinzel", serif;
    font-weight: 600;
    font-size: 19px;
    color: var(--gold);
    line-height: 1.2;
  }
  .person-title {
    font-size: 13px;
    color: var(--title-tint);
    margin-top: 4px;
  }
  .divider {
    position: absolute;
    left: 268px; top: 150px;
    width: 1px; height: 100px;
    background: var(--rule-dark);
  }
  .contact {
    position: absolute;
    left: 290px; top: 148px;
    color: var(--ink-light);
    font-size: 12px;
    line-height: 1.5;
  }
  .contact address { font-style: normal; margin-bottom: 10px; }
  .contact-list { list-style: none; }
  .contact-list li { display: flex; align-items: center; gap: 8px; }
  .contact-icon { width: 11px; height: 11px; flex: none; }
  .card-back {
    left: 625px;
    background: var(--card-white);
  }
  .card-back .brand { top: 52px; }
  .notes { position: absolute; left: 40px; right: 40px; top: 105px; list-style: none; }
  .notes li { height: 34px; border-bottom: 1px dotted var(--dot-rule); }
  .web {
    position: absolute;
    left: 0; right: 0; bottom: 26px;
    text-align: center;
    font-size: 12px;
    letter-spacing: 6px;
    color: var(--ink-dark);
  }
</style>
</head>
<body>
  <section class="card card-front">
    <div class="brand"><span class="brand-mark"></span><span class="brand-name">Stalwart Noble Alloys Foundries</span></div>
    <div class="person">
      <div class="person-name">DANIEL HARROW</div>
      <div class="person-title">President</div>
    </div>
    <div class="divider"></div>
    <div class="contact">
      <address>2740 Linden Crest Rd<br>Marlow, OR 97410</address>
      <ul class="contact-list">
        <li><svg class="contact-icon" viewBox="0 0 12 12"><path d="M3 1l2 2-1 1.5c.6 1.4 1.6 2.4 3 3L8.5 6.5l2 2L9 10.5C5 10 2 7 1.5 3z" fill="var(--gold)"/></svg>(541) 555-0187</li>
        <li><svg class="contact-icon" viewBox="0 0 12 12"><rect x="1" y="2.5" width="10" height="7" fill="var(--gold)"/><path d="M1 2.5l5 4 5-4" stroke="var(--card-black)" fill="none"/></svg>info@stalwartnaf.com</li>
        <li><svg class="contact-icon" viewBox="0 0 12 12"><circle cx="6" cy="6" r="5" fill="var(--gold)"/><path d="M1 6h10M6 1c-2 3-2 7 0 10M6 1c2 3 2 7 0 10" stroke="var(--card-black)" fill="none" stroke-width="0.8"/></svg>stalwartnaf.com</li>
      </ul>
    </div>
  </section>

  <section class="card card-back">
    <div class="brand"><span class="brand-mark"></span><span class="brand-name">Stalwart Noble Alloys Foundries</span></div>
    <ul class="notes"><li></li><li></li><li></li><li></li></ul>
    <div class="web">WWW.STALWARTNAF.COM</div>
  </section>
</body>
</html>
```